Business Card Design

After a corporate career in the finance sector I am now operating on my own as a consultant. I require a simple design, and want a strong card which is targeted at a conservative audience.

Target Market(s)

highly educated senior management, directors of companies, finance sector

Industry/Entity Type

Conservative

Contact Information for Business Card

Rosa Tindell
Consultant
Mobile: 0417 862 254
Email: rosa.tind@mailvora.com

Requirements
Should not have
• I don't want the colours green/yellow/brown

```html
<!DOCTYPE html>
<html lang="en">
<head>
<meta charset="utf-8">
<title>Rosa Tindell – Business Card</title>
<link href="https://fonts.googleapis.com/css2?family=Arimo:wght@400;700&family=Archivo+Narrow:wght@500&display=swap" rel="stylesheet">
<style>
  :root {
    --canvas-bg: #d9d9d6;
    --card-bg: #151515;
    --card-edge: #222222;
    --name-white: #f4f4f4;
    --title-grey: #bdbdbd;
    --rule-grey: #cfcfcf;
    --contact-grey: #c4c4c4;
  }

  html, body {
    margin: 0;
    padding: 0;
    width: 1200px;
    height: 900px;
    overflow: hidden;
    background: var(--canvas-bg);
  }

  .canvas {
    position: relative;
    width: 1200px;
    height: 900px;
  }

  .business-card {
    position: absolute;
    left: 150px;
    top: 185px;
    width: 900px;
    height: 530px;
    background: radial-gradient(ellipse at 40% 35%, #1d1d1d 0%, var(--card-bg) 70%);
    border: 1px solid var(--card-edge);
    box-shadow: 0 14px 40px rgba(0, 0, 0, 0.25);
  }

  .identity {
    position: absolute;
    left: 110px;
    top: 120px;
  }

  .card-name {
    margin: 0;
    font-family: "Arimo", Arial, sans-serif;
    font-weight: 700;
    font-size: 88px;
    line-height: 1;
    color: var(--name-white);
    letter-spacing: 0.5px;
  }

  .card-title {
    margin: 12px 0 0 4px;
    font-family: "Arimo", Arial, sans-serif;
    font-weight: 400;
    font-size: 30px;
    line-height: 1;
    letter-spacing: 0.62em;
    color: var(--title-grey);
  }

  .divider {
    position: absolute;
    left: 100px;
    top: 300px;
    width: 700px;
    height: 4px;
    background: var(--rule-grey);
  }

  .contact {
    position: absolute;
    right: 130px;
    top: 330px;
    text-align: right;
    font-family: "Archivo Narrow", "Arial Narrow", sans-serif;
    font-weight: 500;
    color: var(--contact-grey);
  }

  .contact-phone {
    margin: 0;
    font-size: 52px;
    line-height: 1.1;
    letter-spacing: 2px;
  }

  .contact-email {
    margin: 14px 0 0;
    font-size: 36px;
    line-height: 1.1;
  }
</style>
</head>
<body>
  <main class="canvas">
    <section class="business-card" aria-label="Business card for Rosa Tindell, Consultant">
      <div class="identity">
        <h1 class="card-name">Rosa Tindell</h1>
        <p class="card-title">Consultant</p>
      </div>
      <div class="divider"></div>
      <div class="contact">
        <p class="contact-phone">0417 862 254</p>
        <p class="contact-email">rosa.tind@mailvora.com</p>
      </div>
    </section>
  </main>
</body>
</html>
```